Cd Cover Design needed for Electronic Music album

I need a cd cover design for my new album of Electronic music, sub-genre from Electronic to Techno to Tech-House to Dub-House.(just want people to Dance)
My artist name is "Velvet Circuit" and the album is "Lantern of Tides". I have uploaded an image for artist name ,its just for the idea of how the letters go. Would like to see designs in blue was thinking of Audio equipment or audio wavs (looks like an earthquake meter) ,I am a fan of Masking images and puting another image inside, i would like the design to catch eyes and reach out for different and unique, my music ranges from soft to hard crunch within the same songs. I am excited to see what you come up with.
With many Thanks from Velvet Circuit

I have uploaded 9 Design ideas,dont use the images i do not own them only downloaded, some of the images show the photoshop two image design.

the size and track names are below:

online distributor requires the size of 1448x1448
track font ,something straight and orderly (not to fancy for the lettering)
1. Granite Vs Feather 6:54
2. Lantern of Tides 6:10
3. B N Bold 8:04
4. Never Fadin 7:04
5. Gonna find it 7:15
6. Turn over 5:40
7. Under the Copper bridge 6:38

I would also like to have the designer(s) put on a small section on the inside cover designers contact info and type "designs by:" that way the designer gets some viewer coverage also.

Target Market(s)

Anyone that listens to Electronic / Techno / House / Dub.

Industry/Entity Type

Electronic

Colors
0455a3

Requirements
Must have
• The logo that I uploaded I was hoping that someone could design that better for me not using font style letters but drawn and put that together with the design. Please don't use my design that I uploaded (its not to appealing, its why im not a designer) ,its just to show how I want the letters. Also I like black as the background color.
Nice to have
• Image Masking ,like1, 2 or 3 images in one silhouette image, images done like from the album of Quenford except no squirrels ,Photoshop is a plus, really would like to see designs with real images that are masked with other images.

```html
<!DOCTYPE html>
<html lang="en">
<head>
<meta charset="utf-8">
<title>Velvet Circuit – Lantern of Tides</title>
<link rel="stylesheet" href="https://fonts.googleapis.com/css2?family=Oswald:wght@700&display=swap">
<style>
  :root {
    --deep-blue: #0a2a8c;
    --brand-blue: #0455a3;
    --violet-blue: #3b4fc4;
    --cyan: #39d3f2;
    --aqua-green: #2fe0a8;
    --ice: #bff1ff;
    --ink: #050510;
    --frame-dark: #0b1e7a;
    --meter: #d8f6ff;
  }
  html, body {
    margin: 0;
    padding: 0;
    width: 1200px;
    height: 1200px;
    overflow: hidden;
    background: #000;
  }
  .cover {
    position: relative;
    width: 1200px;
    height: 1200px;
    overflow: hidden;
    font-family: "Oswald", "Arial Narrow", sans-serif;
  }
  .cover__backdrop {
    position: absolute;
    inset: 0;
    background:
      radial-gradient(ellipse 420px 260px at 90px 560px, rgba(47,224,168,0.75), transparent 70%),
      radial-gradient(ellipse 420px 260px at 1110px 560px, rgba(47,224,168,0.7), transparent 70%),
      radial-gradient(ellipse 700px 420px at 600px 520px, rgba(57,211,242,0.55), transparent 75%),
      linear-gradient(180deg, var(--violet-blue) 0%, var(--brand-blue) 45%, var(--deep-blue) 100%);
  }
  .cover__art {
    position: absolute;
    inset: 0;
  }
  .level-meter line {
    stroke: var(--meter);
    stroke-width: 14;
    stroke-dasharray: 7 6;
    opacity: 0.4;
  }
  .artist-name {
    font-family: "Oswald", "Arial Narrow", sans-serif;
    font-weight: 700;
    fill: var(--ink);
    letter-spacing: 4px;
  }
  .album-title {
    font-family: "Oswald", "Arial Narrow", sans-serif;
    font-weight: 700;
    fill: var(--ice);
  }
  .album-title__small {
    font-size: 70px;
  }
</style>
</head>
<body>
  <main class="cover">
    <div class="cover__backdrop" role="img" aria-label="Abstract blue and green smoky light streams"></div>

    <svg class="cover__art" width="1200" height="1200" viewBox="0 0 1200 1200">
      <defs>
        <linearGradient id="inner-fill" x1="0" y1="0" x2="0" y2="1">
          <stop offset="0" stop-color="#7fe6ff" stop-opacity="0.85"/>
          <stop offset="0.55" stop-color="#2fb5ec" stop-opacity="0.75"/>
          <stop offset="1" stop-color="#1463d8" stop-opacity="0.8"/>
        </linearGradient>
        <linearGradient id="outer-fill" x1="0" y1="0" x2="0" y2="1">
          <stop offset="0" stop-color="#1a2aa8" stop-opacity="0.55"/>
          <stop offset="1" stop-color="#0a2a8c" stop-opacity="0.65"/>
        </linearGradient>
        <filter id="title-shadow" x="-10%" y="-10%" width="120%" height="130%">
          <feDropShadow dx="0" dy="4" stdDeviation="5" flood-color="#04206e" flood-opacity="0.8"/>
        </filter>
      </defs>

      <polygon class="frame-outer" points="597,45 15,1080 1190,1078"
               fill="url(#outer-fill)" stroke="var(--frame-dark)" stroke-width="6" stroke-linejoin="round"/>

      <path class="frame-inner"
            d="M580,225 Q600,195 620,225 L1045,965 Q1060,995 1025,995 L175,995 Q140,995 155,965 Z"
            fill="url(#inner-fill)" stroke="#0d2fa8" stroke-width="5"/>

      <g class="level-meter">
        <line x1="180" y1="310" x2="180" y2="720"/>
        <line x1="210" y1="380" x2="210" y2="720"/>
        <line x1="240" y1="340" x2="240" y2="720"/>
        <line x1="270" y1="420" x2="270" y2="720"/>
        <line x1="300" y1="305" x2="300" y2="720"/>
        <line x1="330" y1="360" x2="330" y2="720"/>
        <line x1="360" y1="440" x2="360" y2="720"/>
        <line x1="390" y1="330" x2="390" y2="720"/>
        <line x1="420" y1="400" x2="420" y2="720"/>
        <line x1="450" y1="350" x2="450" y2="720"/>
        <line x1="480" y1="430" x2="480" y2="720"/>
        <line x1="510" y1="320" x2="510" y2="720"/>
        <line x1="540" y1="300" x2="540" y2="720"/>
        <line x1="570" y1="370" x2="570" y2="720"/>
        <line x1="600" y1="330" x2="600" y2="720"/>
        <line x1="630" y1="410" x2="630" y2="720"/>
        <line x1="660" y1="300" x2="660" y2="720"/>
        <line x1="690" y1="350" x2="690" y2="720"/>
        <line x1="720" y1="420" x2="720" y2="720"/>
        <line x1="750" y1="340" x2="750" y2="720"/>
        <line x1="780" y1="390" x2="780" y2="720"/>
        <line x1="810" y1="450" x2="810" y2="720"/>
        <line x1="840" y1="360" x2="840" y2="720"/>
        <line x1="870" y1="410" x2="870" y2="720"/>
        <line x1="900" y1="470" x2="900" y2="720"/>
        <line x1="930" y1="380" x2="930" y2="720"/>
        <line x1="960" y1="440" x2="960" y2="720"/>
        <line x1="990" y1="400" x2="990" y2="720"/>
        <line x1="1020" y1="460" x2="1020" y2="720"/>
      </g>

      <g class="artist-name">
        <text x="215" y="545" font-size="165" textLength="790" lengthAdjust="spacing">VELVET</text>
        <text x="165" y="720" font-size="165" textLength="790" lengthAdjust="spacing">CIRCUIT</text>
      </g>

      <text class="album-title" x="600" y="945" text-anchor="middle" font-size="170"
            textLength="790" lengthAdjust="spacingAndGlyphs" filter="url(#title-shadow)">LANTERN<tspan class="album-title__small" dy="-85">of</tspan><tspan dy="85">TIDES</tspan></text>
    </svg>
  </main>
</body>
</html>
```